Business Card for a mobile physiotherapy company

I need a layout for a business card for a mobile physiotherapy company.
Slogan is "Mobile Physiotherapy - Your Road To Recovery"
Phone number is 867-402-5913
Email VantrePhysio@mailbright.ca (subject to change with website)
Website www.VantrePhysio.ca
My name and credentials: Kent Vantre Kent Vantre, BSc(kin), MPT, CAFCI, IMS
Information maybe included: Direct Billing, Services including Physiotherapy, IMS, acupuncture
Maybe include facebook and instagram logos
One side with the logo clean and sharp
Other side with details, try not to look too busy, keep everything concise

```html
<!DOCTYPE html>
<html lang="en">
<head>
<meta charset="utf-8">
<title>Vantre Physio – Business Card</title>
<link rel="stylesheet" href="https://fonts.googleapis.com/css2?family=Libre+Baskerville:wght@700&family=Source+Sans+3:wght@400;600&display=swap">
<style>
  :root{
    --navy:#2d4a7b;
    --green:#0d5b4b;
    --ink:#222;
    --rule:#cfcfcf;
    --paper:#ffffff;
    --backdrop:#e9eaec;
    --social:#6a6fb5;
  }
  *{margin:0;padding:0;box-sizing:border-box}
  html,body{width:1200px;height:960px;overflow:hidden;background:var(--backdrop)}
  body{position:relative;font-family:"Source Sans 3",Arial,sans-serif;color:var(--ink)}
  .card{position:absolute;left:170px;width:860px;height:440px;background:var(--paper);overflow:hidden;box-shadow:0 4px 14px rgba(0,0,0,.12)}
  .card--front{top:26px}
  .card--back{top:494px}

  .brand{display:flex;align-items:center;justify-content:center;gap:16px;font-family:"Source Sans 3",Arial,sans-serif;font-weight:600;color:var(--navy);line-height:1;white-space:nowrap}
  .brand__dot{width:34px;height:34px;border-radius:50%;background:var(--navy);flex:none}

  .card--front .brand{position:absolute;left:0;right:0;top:150px;font-size:64px}
  .social{position:absolute;left:0;right:0;top:300px;display:flex;justify-content:center;gap:70px;font-size:24px}
  .social__item{display:flex;align-items:center;gap:12px}
  .social__box{width:38px;height:38px;border-radius:6px;background:var(--social)}

  .card--back .brand{position:absolute;left:30px;width:420px;top:110px;font-size:48px;gap:12px}
  .card--back .brand__dot{width:28px;height:28px}
  .wave{position:absolute;inset:0}
  .slogan{font-family:"Libre Baskerville",Georgia,serif;font-weight:700;font-size:19px;fill:#fff}
  .divider{position:absolute;left:470px;top:50px;width:2px;height:230px;background:var(--rule)}
  .details{position:absolute;left:500px;top:48px;width:340px}
  .details__name{font-family:"Libre Baskerville",Georgia,serif;font-weight:700;color:var(--navy);font-size:24px;letter-spacing:1px}
  .details__creds{font-size:15px;margin:2px 0 12px}
  .contact{list-style:none;font-size:21px}
  .contact li{display:flex;align-items:center;gap:10px;line-height:1.4}
  .contact svg{width:18px;height:18px;flex:none}
  .services{margin-top:14px}
  .services__title{font-weight:600;color:var(--navy);font-size:20px}
  .services__list{list-style:none;display:grid;grid-template-columns:auto auto;column-gap:24px;color:var(--green);font-size:20px;line-height:1.3;justify-content:start}
  .services__list li::before{content:"• "}
</style>
</head>
<body>

<section class="card card--front">
  <div class="brand"><span class="brand__dot"></span>Vantre Physio</div>
  <div class="social">
    <div class="social__item"><span class="social__box"></span>VantrePhysio</div>
    <div class="social__item"><span class="social__box"></span>@VantrePhysio</div>
  </div>
</section>

<section class="card card--back">
  <svg class="wave" viewBox="0 0 860 440" width="860" height="440">
    <path d="M0,222 C230,226 520,300 760,440 L730,440 C500,310 230,244 0,240 Z" fill="var(--green)"/>
    <path d="M0,252 C220,258 480,326 700,440 L0,440 Z" fill="var(--navy)"/>
    <path id="sloganPath" d="M40,292 C230,300 430,352 640,440" fill="none"/>
    <text class="slogan"><textPath href="#sloganPath">Mobile Physiotherapy - Your Road To Recovery</textPath></text>
  </svg>

  <div class="brand"><span class="brand__dot"></span>Vantre Physio</div>

  <div class="divider"></div>

  <div class="details">
    <div class="details__name">KENT VANTRE</div>
    <div class="details__creds">BSc(kin), MPT, CAFCI, IMS</div>
    <ul class="contact">
      <li><svg viewBox="0 0 20 20"><circle cx="10" cy="10" r="9" fill="none" stroke="#333" stroke-width="1.6"/><path d="M7 5.5l2 2-1 1.3a6 6 0 0 0 3.2 3.2l1.3-1 2 2-1.3 1.5C10 14 6 10 5.5 6.8z" fill="#333"/></svg>867-402-5913</li>
      <li><svg viewBox="0 0 20 20"><circle cx="10" cy="10" r="9" fill="none" stroke="#333" stroke-width="1.6"/><rect x="5" y="6.5" width="10" height="7" fill="none" stroke="#333" stroke-width="1.4"/><path d="M5 6.5l5 4 5-4" fill="none" stroke="#333" stroke-width="1.4"/></svg>VantrePhysio@mailbright.ca</li>
      <li><svg viewBox="0 0 20 20"><circle cx="10" cy="10" r="9" fill="none" stroke="#333" stroke-width="1.6"/><ellipse cx="10" cy="10" rx="4" ry="9" fill="none" stroke="#333" stroke-width="1.3"/><path d="M1 10h18M3 5.5h14M3 14.5h14" stroke="#333" stroke-width="1.3"/></svg>www.VantrePhysio.ca</li>
    </ul>
    <div class="services">
      <div class="services__title">Services Including</div>
      <ul class="services__list">
        <li>Physiotherapy</li>
        <li>Direct Billing</li>
        <li>Ims</li>
        <li>Acupuncture</li>
      </ul>
    </div>
  </div>
</section>

</body>
</html>
```